Kids support program needs a postcard design

We support children who have parents with mental health issues.
We teach them skills that help them grow in hope, resilience, and happiness.
We use cartoons and slogans/saying so they can remember useful skills to use in their daily lives.
We want to put a bunch of these sayings/slogans onto a card to give out to kids.

Just letting you know I uploaded a few more files that now have the slogans typed up so you dont need to type these from the previous handwritten doc.

Also I have included the two logos I want on the front and the other on the back page.
Also I have attached a photo of the look and feel I was generally looking for
many thanksĀ 

Target Market(s)

kids and teenagers

Industry/Entity Type

Mental Health

Requirements
Must have
• 2 pages
include the words I send you (please note I will need to add and delete and modify several words once I have seen what you have produced),
plus include the logos I send you and also two cartoons that I send you (therefore please save space for 4 other bits).
Page one (tobralin) has colored writing in various shades of green, but the dominant color being an emerald greeen. This program is a wellness program - growing, organic
the second page would be in red (with maroon tinge). This program is a Meditation program - warm, spacious feel.
each page should have various types of font, sometimes in capitals, with writing being different size, most going horizontal but some vertical, also some with color in background and words in white).
In the 2 attached docs you will see what I have in mind - note each attachment represents one side of the card (hence two sides of the card).
I have also attached a doc with the slogans typed up - please note these are the actual words to put in the card (not the handwritten words in the other two docs)
I plan to print these in A4 size and also in postcard size (please note this for font size so it is clearly readable)
I have attached an example of the type of look and feel I would like the card to have

```html
<!DOCTYPE html>
<html lang="en">
<head>
<meta charset="utf-8">
<title>Mirevale – Meditation Slogans Card</title>
<link rel="stylesheet" href="https://fonts.googleapis.com/css2?family=Cinzel:wght@400;700&family=Great+Vibes&family=Rye&family=Oswald:wght@400;600;700&family=Poiret+One&family=Playfair+Display:ital,wght@1,700;1,900&family=Josefin+Sans:wght@300;400;600&family=Abril+Fatface&family=Alfa+Slab+One&family=Courier+Prime&family=Arimo:wght@400;700&family=Dancing+Script:wght@600&family=Special+Elite&family=Raleway:wght@400;600&display=swap">
<style>
  :root {
    --maroon: #a8123e;
    --paper: #ffffff;
  }
  * { box-sizing: border-box; margin: 0; padding: 0; }
  html, body { width: 857px; height: 1200px; overflow: hidden; background: var(--paper); }
  .card {
    position: relative;
    width: 857px; height: 1200px;
    background: var(--paper);
    color: var(--maroon);
    overflow: hidden;
  }
  .slogans {
    position: absolute;
    left: 18px; top: 14px;
    width: 598px; height: 1176px;
    display: flex; flex-direction: column;
    justify-content: space-between;
  }
  .line { white-space: nowrap; line-height: 1; }
  .sm { font-size: 0.7em; }

  .l-light { font-family: 'Cinzel', serif; font-weight: 700; font-size: 25px; letter-spacing: 1px; }
  .l-compassion { font-family: 'Arimo', sans-serif; font-size: 25px; }
  .l-compassion .script { font-family: 'Great Vibes', cursive; font-size: 28px; }
  .l-humanity { font-family: 'Rye', serif; font-size: 42px; letter-spacing: 5px; }
  .l-beginner { font-family: 'Oswald', sans-serif; font-weight: 700; font-size: 27px; }
  .l-beginner .soft { font-family: 'Arimo', sans-serif; font-weight: 400; font-size: 29px; }
  .l-beginner em { font-family: 'Dancing Script', cursive; font-size: 32px; }
  .l-breathe { font-family: 'Poiret One', sans-serif; font-size: 29px; font-weight: 700; }
  .l-count { font-family: 'Oswald', sans-serif; font-weight: 600; font-size: 30px; }
  .l-whole { font-family: 'Playfair Display', serif; font-style: italic; font-weight: 900; font-size: 35px; }
  .l-focus { font-family: 'Josefin Sans', sans-serif; font-weight: 300; font-size: 37px; letter-spacing: 1px; }
  .l-arriving { font-family: 'Cinzel', serif; font-size: 26px; }
  .l-arriving .script { font-family: 'Great Vibes', cursive; font-size: 27px; }
  .l-may { font-family: 'Poiret One', sans-serif; font-weight: 700; font-size: 32px; }
  .l-mind { font-family: 'Alfa Slab One', serif; font-size: 20px; }
  .l-wishing { font-family: 'Great Vibes', cursive; font-size: 38px; }

  .senses-row { display: flex; justify-content: space-between; align-items: flex-end; }
  .senses-left { display: flex; flex-direction: column; gap: 8px; }
  .senses-right { display: flex; flex-direction: column; align-items: center; }
  .l-company { font-family: 'Arimo', sans-serif; font-size: 23px; }
  .l-kindly { font-family: 'Cinzel', serif; font-size: 17px; font-weight: 700; }
  .l-remember { font-family: 'Josefin Sans', sans-serif; font-size: 25px; font-weight: 600; }
  .l-coming { font-family: 'Arimo', sans-serif; font-size: 31px; }
  .l-senses { font-family: 'Josefin Sans', sans-serif; font-weight: 300; font-size: 56px; letter-spacing: 2px; }

  .l-loving { font-family: 'Cinzel', serif; font-size: 27px; }
  .l-savour { font-family: 'Great Vibes', cursive; font-size: 50px; letter-spacing: 2px; }
  .l-present { font-family: 'Oswald', sans-serif; font-size: 26px; }
  .l-meditation { font-family: 'Special Elite', system-ui; font-size: 31px; }
  .l-justlike { font-family: 'Oswald', sans-serif; font-weight: 600; font-size: 36px; }
  .l-justlike .script { font-family: 'Great Vibes', cursive; font-size: 38px; font-weight: 400; }
  .l-spacious { font-family: 'Alfa Slab One', serif; font-size: 53px; letter-spacing: 7px; }
  .l-suffering { font-family: 'Arimo', sans-serif; font-size: 35px; }
  .l-moment { font-family: 'Abril Fatface', serif; font-style: italic; font-size: 19px; }
  .l-moment .caps { font-family: 'Courier Prime', monospace; font-style: normal; font-size: 27px; letter-spacing: 2px; }
  .l-soft { font-family: 'Rye', serif; font-size: 38px; letter-spacing: 1px; }
  .l-sensations { font-family: 'Courier Prime', monospace; font-size: 26px; }
  .l-recognise { font-family: 'Great Vibes', cursive; font-size: 31px; }
  .l-ride { font-family: 'Rye', serif; font-size: 28px; }
  .l-ride .deep { font-family: 'Oswald', sans-serif; font-size: 30px; }
  .l-heart { font-family: 'Arimo', sans-serif; font-weight: 700; font-size: 31px; }
  .l-heart em { font-style: italic; }
  .l-yourself { font-family: 'Courier Prime', monospace; font-size: 27px; letter-spacing: 2px; }
  .l-cultivate { font-family: 'Great Vibes', cursive; font-size: 42px; }
  .l-cultivate .caps { font-family: 'Cinzel', serif; font-size: 32px; }

  .program-name {
    position: absolute;
    left: 605px; top: 40px;
    width: 120px; height: 470px;
    display: flex; flex-direction: column; align-items: center; justify-content: center; gap: 18px;
  }
  .program-name .word {
    writing-mode: vertical-rl;
    transform: rotate(180deg);
    font-family: 'Alfa Slab One', serif;
    font-size: 62px;
    color: var(--maroon);
    letter-spacing: 2px;
  }
  .program-name .mark {
    width: 22px; height: 22px; background: var(--maroon);
  }
</style>
</head>
<body>
<main class="card">
  <section class="slogans" aria-label="Meditation slogans">
    <p class="line l-light">Discover &amp; share your LIGHT</p>
    <p class="line l-compassion"><span class="script">Self-compassion</span>... Mindfulness... Self-kindness</p>
    <p class="line l-humanity">shared humanity</p>
    <p class="line l-beginner">BEGINNER'S MIND <span class="soft">Welcome <em>all</em> visitors</span></p>
    <p class="line l-breathe">BREATHE DEEPLY to calm the barking dog</p>
    <p class="line l-count">OUT-BREATH Count In-BREATH Count</p>
    <p class="line l-whole">WHOLE BODY BREATHING</p>
    <p class="line l-focus">FOCUS ON A SINGLE POINT</p>
    <p class="line l-arriving">Arriving at your door <span class="script">5 Colors Shapes Sounds</span></p>
    <p class="line l-may">MAY I BE ... Happy Healthy Well</p>
    <p class="line l-mind">MIND HEART BODY LIKE SKY OCEAN MOUNTAIN</p>
    <p class="line l-wishing">Wishing Ourselves &amp; Others Well</p>
    <div class="senses-row">
      <div class="senses-left">
        <p class="line l-company">Good company for the journey</p>
        <p class="line l-kindly">KINDLY, GENTLY RETURN TO THE BREATH</p>
        <p class="line l-remember">REMEMBER YOU ARE LOVED</p>
      </div>
      <div class="senses-right">
        <p class="line l-coming">coming to our</p>
        <p class="line l-senses">SENSES</p>
      </div>
    </div>
    <p class="line l-loving">Loving-kindness Imagery Feeling Words</p>
    <p class="line l-savour">Savour sitting well</p>
    <p class="line l-present">Present moment awareness... kind, curious, accepting</p>
    <p class="line l-meditation">Meditation ... it's not what you think</p>
    <p class="line l-justlike">Just like me <span class="script">Circle of compassion</span></p>
    <p class="line l-spacious">SPACIOUSNESS</p>
    <p class="line l-suffering">Suffering = Pain x Resistance</p>
    <p class="line l-moment">Every moment is a chance <span class="caps">TAKE IN THE GOOD</span></p>
    <p class="line l-soft">SOFT EYES, SOFT FACE</p>
    <p class="line l-sensations">Sensations, Images, Feelings, Thoughts</p>
    <p class="line l-recognise">Recognise, Accept, Inquire, Non-identify, let go</p>
    <p class="line l-ride">RIDE THE BREATH <span class="deep">Deep RESOLVE</span></p>
    <p class="line l-heart">Take care of your <em>GOOD HEART</em></p>
    <p class="line l-yourself">BE GOOD COMPANY FOR YOURSELF</p>
    <p class="line l-cultivate">Cultivate <span class="caps">LOVE</span> &amp; <span class="caps">WISDOM</span></p>
  </section>

  <aside class="program-name" aria-label="Mirevale">
    <span class="mark"></span>
    <span class="word">Mirevale</span>
  </aside>
</main>
</body>
</html>
```